Financial e-service company needs a landing page

We need a landing page for a new start up Company.
We offer Electronic gift Cards.
We are using the primiraly the colours blue and white on our homepage. Our product is a new simple and serious financial payment way, so we need a landing page that gives a serious, professional and trustworthy look.
We are using normal browsers and would like the landing page to be scalable to different devices (tablet, phone).
In our topbar we have (se the uploaded files):
- The Company name = Glimtkassen.dk
- A home button = Hjem
- About Glimtkassen = Om Glimtkassen
- Contact us = kontakt os
- Redeem giftcard = indløs pengegave
- Sign me up = opret mig
- Log in botton = log på
At the center of the homepage we have different choice of giftcards solution as which the buyer can chose among.
- Print your personel giftcard (print selv)
- Electronic giftcard (elektronisk)
- Already have card (har kort)
I have attached our present logo - Glimtkassen by Kestrel Nine. There is a little story why the mother company is called Kestrel Nine instead of Money tree. It is because the company is started by three young guys.
Target Market(s)
Primiraly private individuals
Industry/Entity Type
Financial Service
Coding
Coded - Design and coding required
Number of Pages Required
1 page
Requirements
Must have
- - A top menu bar
- - a picture/drawning/figure (instead of the box - se screendump of homepage)
- - 3 different product choices - Print selv, Elektronisk and Har kort (se screendump homepage 1)
- - The prices of 3 different products (se screendump homepage 1)
Nice to have
- We have discused that maybe it would nice to have a log in box at the landing page, so it is for new users to sign up.
- We are open for other user minded suggestions

```html
<!DOCTYPE html>
<html lang="da">
<head>
<meta charset="utf-8">
<title>Glimtkassen – elektroniske gavekort</title>
<link rel="stylesheet" href="https://fonts.googleapis.com/css2?family=Lato:wght@400;700&family=Montserrat:wght@400;500&family=Roboto:wght@300;400&display=swap">
<style>
  :root {
    --blue: #3aa3d8;
    --white: #ffffff;
    --ink: #3c3c3c;
    --hero-dark: #1c2a38;
    --hero-warm: #5a4534;
    --line: rgba(255,255,255,0.18);
  }
  * { box-sizing: border-box; margin: 0; padding: 0; }
  html, body { width: 1200px; height: 1200px; overflow: hidden; background: var(--white); }
  body { position: relative; font-family: "Roboto", sans-serif; }

  .hero {
    position: absolute; left: 0; top: 0; width: 1200px; height: 648px;
    background:
      radial-gradient(ellipse 420px 300px at 620px 260px, rgba(150,110,85,0.55), transparent 70%),
      radial-gradient(ellipse 360px 220px at 420px 380px, rgba(40,110,140,0.55), transparent 70%),
      linear-gradient(160deg, #22303d 0%, var(--hero-dark) 40%, var(--hero-warm) 75%, #241c17 100%);
  }

  .topbar {
    position: absolute; left: 0; top: 0; width: 1200px; height: 56px;
    border-bottom: 1px solid var(--line);
  }
  .topbar a {
    position: absolute; top: 18px;
    font-family: "Montserrat", sans-serif; font-size: 14px;
    color: var(--white); text-decoration: none; white-space: nowrap;
  }
  .topbar .active::after {
    content: ""; position: absolute; left: -21px; right: -19px; top: 37px;
    height: 1px; background: var(--white);
  }
  .search { position: absolute; left: 1029px; top: 18px; }

  .brand {
    position: absolute; left: 0; width: 1200px; top: 110px; text-align: center;
  }
  .brand-dot {
    display: inline-block; width: 22px; height: 22px; border-radius: 50%;
    border: 2px solid var(--white); margin-bottom: 12px;
  }
  .brand-name {
    font-family: "Lato", sans-serif; font-weight: 700; font-size: 20px;
    color: var(--white); letter-spacing: 1px;
  }

  .hero-title {
    position: absolute; left: 340px; width: 586px; top: 296px;
    text-align: center; font-family: "Lato", sans-serif; font-weight: 700;
    font-size: 29px; line-height: 39px; color: var(--white); text-transform: uppercase;
  }
  .hero-text {
    position: absolute; left: 390px; width: 486px; top: 379px;
    text-align: center; font-weight: 300; font-size: 14.5px; line-height: 22.4px;
    color: var(--white); letter-spacing: 0.3px;
  }
  .cta {
    position: absolute; left: 525px; top: 468px; width: 216px; height: 34px;
    border-radius: 17px; background: var(--blue); color: var(--white);
    font-family: "Lato", sans-serif; font-weight: 700; font-size: 14px;
    line-height: 34px; text-align: center;
  }
  .scroll-down { position: absolute; left: 614px; top: 591px; }

  .offers { position: absolute; left: 0; top: 648px; width: 1200px; height: 383px; }
  .offer {
    position: absolute; top: 104px; width: 220px; margin-left: -110px; text-align: center;
  }
  .offer svg { display: block; margin: 0 auto; height: 52px; }
  .offer h3 {
    margin-top: 5px; font-family: "Lato", sans-serif; font-weight: 400;
    font-size: 14.5px; color: var(--blue); text-transform: uppercase;
  }
  .offer p {
    margin-top: 3px; font-size: 11.5px; line-height: 22.4px; color: var(--ink);
    letter-spacing: 0.3px;
  }
  .price {
    display: inline-block; margin-top: 10px; width: 78px; height: 24px;
    border-radius: 12px; background: var(--blue); color: var(--white);
    font-family: "Lato", sans-serif; font-weight: 700; font-size: 11px;
    line-height: 24px; letter-spacing: 0.5px;
  }

  .workspace {
    position: absolute; left: 0; top: 1031px; width: 1200px; height: 169px;
    background: linear-gradient(90deg, #a9a9a7 0%, #c9c8c5 45%, #bdbcb8 80%, #b7ae6a 100%);
  }
  .workspace-ring {
    position: absolute; left: 599px; top: 1148px; width: 68px; height: 68px;
    border-radius: 50%; border: 2px solid var(--white);
  }
</style>
</head>
<body>
  <section class="hero" role="img" aria-label="Foto af en hånd der rækker et blåt betalingskort frem"></section>

  <nav class="topbar">
    <a class="active" href="#" style="left:291px">Hjem</a>
    <a href="#" style="left:376px">Om Glimtkassen</a>
    <a href="#" style="left:536px">kontakt os</a>
    <a href="#" style="left:654px">indløs pengegave</a>
    <a href="#" style="left:819px">opret mig</a>
    <a href="#" style="left:934px">log på</a>
    <svg class="search" width="18" height="18" viewBox="0 0 18 18" fill="none" stroke="#fff" stroke-width="1.8">
      <circle cx="8" cy="8" r="6.5"/><line x1="12.8" y1="12.8" x2="17" y2="17"/>
    </svg>
  </nav>

  <div class="brand">
    <span class="brand-dot"></span>
    <div class="brand-name">Glimtkassen by Kestrel Nine</div>
  </div>

  <h1 class="hero-title">We offer magnificent electronic gift cards</h1>
  <p class="hero-text">Duis aute irure dolor in reprehenderit in voluptate velit esse cillum dolore eu fugiat nulla pariatur. Excepteur sint occaecat cupidatat non proident, sunt in culpa qui officia deserunt mollit anim id est laborum.</p>
  <div class="cta">SEE OFFERS</div>

  <svg class="scroll-down" width="38" height="38" viewBox="0 0 38 38" fill="none" stroke="#fff" stroke-width="1.6">
    <circle cx="19" cy="19" r="17.5"/><polyline points="14,17 19,22 24,17"/>
  </svg>

  <section class="offers">
    <div class="offer" style="left:394px">
      <svg viewBox="0 0 54 54" width="54" fill="none" stroke="#3aa3d8" stroke-width="1.6">
        <rect x="10" y="1" width="34" height="10"/>
        <rect x="1" y="11" width="52" height="32" rx="4"/>
        <circle cx="41" cy="18" r="1.6"/><circle cx="47" cy="18" r="1.6"/>
        <rect x="10" y="30" width="34" height="23"/>
        <line x1="16" y1="38" x2="26" y2="38"/><line x1="16" y1="43" x2="38" y2="43"/><line x1="16" y1="48" x2="38" y2="48"/>
      </svg>
      <h3>Print selv</h3>
      <p>Lorem ipsum dolor sit amet, consec-tetur adipisicing elit, sed do eiusmod tempor incididunt</p>
      <span class="price">15 DKK</span>
    </div>
    <div class="offer" style="left:628px">
      <svg viewBox="0 0 54 54" width="54" fill="none" stroke="#3aa3d8" stroke-width="1.6">
        <rect x="1" y="10" width="52" height="38"/>
        <polyline points="1,10 27,32 53,10"/>
        <line x1="1" y1="48" x2="21" y2="28"/><line x1="53" y1="48" x2="33" y2="28"/>
      </svg>
      <h3>Elektronisk</h3>
      <p>Lorem ipsum dolor sit amet, consec-tetur adipisicing elit, sed do eiusmod tempor incididunt</p>
      <span class="price">25 DKK</span>
    </div>
    <div class="offer" style="left:862px">
      <svg viewBox="0 0 54 54" width="54" fill="none" stroke="#3aa3d8" stroke-width="1.6">
        <rect x="1" y="10" width="52" height="38" rx="2"/>
        <line x1="1" y1="18" x2="53" y2="18"/><line x1="1" y1="24" x2="53" y2="24"/>
        <line x1="9" y1="36" x2="21" y2="36"/><line x1="9" y1="40" x2="17" y2="40"/>
        <line x1="25" y1="36" x2="31" y2="36"/>
        <rect x="38" y="34" width="6" height="5"/>
      </svg>
      <h3>Har kort</h3>
      <p>Lorem ipsum dolor sit amet, consec-tetur adipisicing elit, sed do eiusmod tempor incididunt</p>
      <span class="price">10 DKK</span>
    </div>
  </section>

  <section class="workspace" role="img" aria-label="Foto af et skrivebord med tastatur, mus og et gult ur"></section>
  <div class="workspace-ring"></div>
</body>
</html>
```